Web Design Business Card

I need a new business card designed, we recently rebranded and I need to get a fresh design to match our new logo, colours and branding.

Details:

Dorian Keeble | Founder & CEO
Address: 7 Fernhollow Lane, #04-09 Maplecrest Vale, Singapore 583104
Tel: +65 93468120
Web: www.plumtrove.com.sg
hello@plumtrove.com.sg

I've attached my old card as well

Requirements
Must have
• Front and Back
Interesting use of logo
Correct use of colour scheme

```html
<!DOCTYPE html>
<html lang="en">
<head>
<meta charset="utf-8">
<title>Plumtrove Business Card</title>
<link rel="stylesheet" href="https://fonts.googleapis.com/css2?family=Ubuntu:wght@500;700&family=Open+Sans:wght@400;600;700&display=swap">
<style>
  :root {
    --stage: #efece6;
    --card: #e8e7e2;
    --card-edge: #c9c7c0;
    --blue: #0aaaea;
    --blue-soft: #cfe3e8;
    --taupe: #6e6560;
    --ink: #5a524d;
    --rule: #8a8682;
    --white: #ffffff;
  }
  * { box-sizing: border-box; margin: 0; padding: 0; }
  html, body { width: 1200px; height: 1000px; overflow: hidden; }
  body { background: var(--stage); position: relative; font-family: "Open Sans", Arial, sans-serif; }

  .card {
    position: absolute;
    background: var(--card);
    border: 1px solid var(--card-edge);
    box-shadow: 0 4px 12px rgba(0,0,0,.18);
    overflow: hidden;
  }
  .card--back { left: 347px; top: 87px; width: 728px; height: 415px; }
  .card--front { left: 94px; top: 415px; width: 729px; height: 415px; }

  .brand { position: absolute; display: flex; align-items: center; }
  .brand__dot { border-radius: 50%; background: var(--blue); flex: none; }
  .brand__text { display: flex; flex-direction: column; }
  .brand__name { font-family: "Ubuntu", Arial, sans-serif; font-weight: 500; color: var(--taupe); line-height: 1; }
  .brand__tag { font-family: "Open Sans", Arial, sans-serif; font-weight: 700; color: var(--blue); letter-spacing: .02em; }

  .card--back .brand { left: 220px; top: 160px; }
  .card--back .brand__dot { width: 78px; height: 78px; margin-right: 13px; }
  .card--back .brand__name { font-size: 46px; }
  .card--back .brand__tag { font-size: 11.5px; margin-top: 6px; }

  .card--front .brand { left: 45px; top: 41px; }
  .card--front .brand__dot { width: 41px; height: 41px; margin-right: 8px; }
  .card--front .brand__name { font-size: 25px; }
  .card--front .brand__tag { font-size: 6.4px; margin-top: 3px; }

  .holder { position: absolute; left: 457px; top: 30px; }
  .holder__name { font-family: "Ubuntu", Arial, sans-serif; font-weight: 700; font-size: 34px; color: var(--blue); letter-spacing: .03em; line-height: 1.05; }
  .holder__role { font-family: "Ubuntu", Arial, sans-serif; font-weight: 500; font-size: 22px; color: var(--ink); line-height: 1; }

  .scrollbar { position: absolute; left: 713px; top: 0; width: 1px; height: 100%; background: var(--card-edge); }
  .scrollbar__thumb { position: absolute; left: 716px; top: 40px; width: 9px; height: 60px; border-radius: 5px; background: var(--blue); }

  .cursor { position: absolute; left: 195px; top: 84px; width: 12px; height: 18px; }

  .rule { position: absolute; left: 0; width: 712px; height: 1px; background: var(--rule); }
  .rule--top { top: 177px; }
  .rule--bottom { top: 319px; }

  .watermark-circle { position: absolute; left: 4px; top: 240px; width: 270px; height: 270px; border-radius: 50%; background: var(--blue-soft); }

  .field { position: absolute; top: 157px; }
  .field__label { font-weight: 700; font-size: 10.5px; color: var(--ink); letter-spacing: .02em; }
  .field__value {
    position: absolute; top: 45px; left: -1px;
    background: var(--blue); color: var(--white);
    font-size: 12.5px; line-height: 18px; padding: 6px 8px 7px;
    white-space: nowrap;
  }
  .field__value::before {
    content: ""; position: absolute; left: 15px; top: -9px;
    border-left: 7px solid transparent; border-right: 7px solid transparent; border-bottom: 9px solid var(--blue);
  }
  .field--email { left: 36px; }   .field--email .field__value { width: 160px; }
  .field--web { left: 209px; }    .field--web .field__value { width: 160px; }
  .field--contact { left: 381px; } .field--contact .field__value { width: 148px; padding-left: 11px; }
  .field--address { left: 542px; } .field--address .field__value { width: 148px; white-space: normal; line-height: 18px; padding: 5px 9px 6px; }
</style>
</head>
<body>

<section class="card card--back" aria-label="Card back">
  <div class="brand">
    <span class="brand__dot"></span>
    <div class="brand__text">
      <span class="brand__name">plumtrove</span>
      <span class="brand__tag">WEB DESIGN &amp; CONSULTANCY</span>
    </div>
  </div>
</section>

<section class="card card--front" aria-label="Card front">
  <div class="watermark-circle"></div>

  <div class="brand">
    <span class="brand__dot"></span>
    <div class="brand__text">
      <span class="brand__name">plumtrove</span>
      <span class="brand__tag">WEB DESIGN &amp; CONSULTANCY</span>
    </div>
  </div>

  <svg class="cursor" viewBox="0 0 12 18" aria-hidden="true">
    <path d="M1 1 L1 14 L4.2 11 L6.6 16.5 L8.4 15.7 L6.1 10.4 L10.5 10.4 Z" fill="#2b2b2b" stroke="#ffffff" stroke-width="1"/>
  </svg>

  <div class="holder">
    <p class="holder__name">Dorian Keeble</p>
    <p class="holder__role">Founder</p>
  </div>

  <div class="rule rule--top"></div>
  <div class="rule rule--bottom"></div>

  <div class="field field--email">
    <p class="field__label">EMAIL</p>
    <p class="field__value">www.plumtrove.com.sg</p>
  </div>
  <div class="field field--web">
    <p class="field__label">WEB SITE</p>
    <p class="field__value">hello@plumtrove.com.sg</p>
  </div>
  <div class="field field--contact">
    <p class="field__label">CONTACT</p>
    <p class="field__value">+65&nbsp; 9346 8120</p>
  </div>
  <div class="field field--address">
    <p class="field__label">ADDRESS</p>
    <p class="field__value">7 Fernhollow Lane,<br>#04-09 Maplecrest Vale,<br>Singapore 583104</p>
  </div>

  <div class="scrollbar"></div>
  <div class="scrollbar__thumb"></div>
</section>

</body>
</html>
```